Business card representing 2 natural foods companies!

Would love a business card that represents the 2 companies that I manage, PressVia and Tamberly Crisp Leaf Co. Clearly, they are both premium food brands that have a cool, modern but classic feel.
I'm open to ideas for how to represent on 1 business card that I am Founder and President of both companies.
Contact Information for Business Card
Logos for both brands, and I think the most important thing is 2 different websites for each company (and perhaps 2 different emails for both companies)
sippressvia.com
mort@sippressvia.com
tamberlycrisp.co
mort@tamberlycrisp.co
Address isn't needed. I think phone number is good:
just cell: 555-874-3190
Also thinking is it possible to include a black ProLinka QR code? I think that would be really cool to include.
Look and feel

```html
<!DOCTYPE html>
<html lang="en">
<head>
<meta charset="utf-8">
<title>PressVia &amp; Tamberly Crisp Leaf Co. — Business Cards</title>
<link rel="stylesheet" href="https://fonts.googleapis.com/css2?family=Lato:wght@300;400;700;900&family=Playfair+Display:wght@700&display=swap">
<style>
  :root {
    --backdrop: #9a9a9a;
    --card-light: #f7f6f3;
    --card-dark: #2f2a2b;
    --ink: #1c1c1c;
    --ink-soft: #8a8a8a;
    --paper-text: #f4f2f0;
    --paper-soft: #d8d4d2;
  }
  * { box-sizing: border-box; margin: 0; padding: 0; }
  html, body {
    width: 1200px; height: 900px; overflow: hidden;
    background: var(--backdrop);
    font-family: "Lato", sans-serif;
  }
  .canvas {
    position: relative; width: 1200px; height: 900px;
  }
  .card {
    position: absolute; left: 250px; width: 700px; height: 400px;
    box-shadow: 0 10px 30px rgba(0,0,0,.25);
  }
  .card--press { top: 40px; background: var(--card-light); color: var(--ink); }
  .card--leaf { top: 460px; background: var(--card-dark); color: var(--paper-text); }

  .brand {
    position: absolute; top: 50%; transform: translateY(-50%);
    font-family: "Lato", sans-serif; font-weight: 900;
    letter-spacing: 2px; text-transform: uppercase;
  }
  .card--press .brand { left: 70px; font-size: 44px; color: var(--ink); }
  .card--leaf .brand {
    left: 60px; width: 280px; text-align: center;
    font-size: 30px; line-height: 1.2; color: var(--paper-text);
    display: flex; flex-direction: column; align-items: center; gap: 14px;
  }
  .brand-ring {
    width: 34px; height: 34px; border: 3px solid var(--paper-text); border-radius: 50%;
  }

  .details {
    position: absolute; top: 88px; font-size: 14px; line-height: 1.45;
  }
  .card--press .details { left: 380px; }
  .card--leaf .details { left: 400px; }
  .person { font-weight: 700; font-size: 16px; line-height: 1.2; }
  .card--leaf .person { font-family: "Playfair Display", serif; font-size: 17px; }
  .role { font-weight: 400; color: var(--ink-soft); font-size: 14px; }
  .card--leaf .role { color: var(--paper-soft); }
  .rule { width: 26px; height: 1px; margin: 16px 0 14px; background: var(--ink-soft); }
  .card--leaf .rule { background: var(--paper-soft); }
  .address { color: var(--ink-soft); font-weight: 300; }
  .card--leaf .address { color: var(--paper-text); font-weight: 400; }
  .contacts { list-style: none; margin-top: 14px; color: var(--ink-soft); font-weight: 300; }
  .card--leaf .contacts { color: var(--paper-text); font-weight: 400; }
  .contacts li { display: flex; align-items: center; gap: 10px; }
  .contacts svg { width: 11px; height: 11px; flex: none; fill: none; stroke: currentColor; stroke-width: 1.6; }
</style>
</head>
<body>
<main class="canvas">

  <section class="card card--press">
    <div class="brand">PressVia</div>
    <div class="details">
      <p class="person">Mort Delaney</p>
      <p class="role">Founder</p>
      <div class="rule"></div>
      <p class="address">PressVia<br>742 Wrenfield Ave.<br>Harlow, OR 97211</p>
      <ul class="contacts">
        <li><svg viewBox="0 0 12 12"><path d="M2 1.5h2.2l1 2.6-1.4 1a6 6 0 0 0 3 3l1-1.4 2.7 1V10a1 1 0 0 1-1 1A9 9 0 0 1 1 2.5a1 1 0 0 1 1-1z"/></svg>(555) 210-0486</li>
        <li><svg viewBox="0 0 12 12"><rect x="1" y="2.5" width="10" height="7"/><path d="M1 2.5l5 4 5-4"/></svg>hello@sippressvia.com</li>
        <li><svg viewBox="0 0 12 12"><circle cx="6" cy="6" r="5"/><path d="M1 6h10M6 1c2.5 2.8 2.5 7.2 0 10M6 1c-2.5 2.8-2.5 7.2 0 10"/></svg>www.sippressvia.com</li>
      </ul>
    </div>
  </section>

  <section class="card card--leaf">
    <div class="brand"><span class="brand-ring"></span>Tamberly Crisp Leaf Co.</div>
    <div class="details">
      <p class="person">Mort Delaney</p>
      <p class="role">President</p>
      <div class="rule"></div>
      <p class="address">Tamberly Crisp Leaf<br>742 Wrenfield Ave.<br>Harlow, OR 97211</p>
      <ul class="contacts">
        <li><svg viewBox="0 0 12 12"><path d="M2 1.5h2.2l1 2.6-1.4 1a6 6 0 0 0 3 3l1-1.4 2.7 1V10a1 1 0 0 1-1 1A9 9 0 0 1 1 2.5a1 1 0 0 1 1-1z"/></svg>(123) 456-7890</li>
        <li><svg viewBox="0 0 12 12"><rect x="1" y="2.5" width="10" height="7"/><path d="M1 2.5l5 4 5-4"/></svg>hello@tamberlycrisp.co</li>
        <li><svg viewBox="0 0 12 12"><circle cx="6" cy="6" r="5"/><path d="M1 6h10M6 1c2.5 2.8 2.5 7.2 0 10M6 1c-2.5 2.8-2.5 7.2 0 10"/></svg>www.tamberlycrisp.co</li>
      </ul>
    </div>
  </section>

</main>
</body>
</html>
```